Honey Bottle Labels for Honey Business

The honey is a niche product and the logo should exude a strong impression of wild and raw honey and natural – as in natural beekeeping. We try to keep things as simple as possible; this includes the processes the honey goes through.
We are looking for something with a gourmet / classy upmarket look and feel design. For example: Ideas with bees, honeycomb, modern or hexagonal feature; something eye catching, but not too busy.
Our honey is all natural and organic. We are a clean, simple yet sophisticated business, so would like our logo to reflect these principles.

Feel free to expand your creativity to anything you may think would look awesome and original!

The label needs to contain:
1. Our company logo. (Please see attached)
2. 100% Pure Raw Honey / Local
3. Net Wt: 16 oz (454 g) (this is the weight of the honey and will need to be modified based on bottle size.)
4. Address, Cedar Ridge, MN 56410 (not larger than 1/16th inch)

Needs to be versatile to include possibility of clear label, I have included some example pictures as ideas (oval, round, square tags)

Sizes needed:
Large oval 2 5/8" x 4 1/2"
Small oval: 1 3/4" wide x 3" tall
Rectangle 1 3/4" tall x 5" wide
Round diameter 2.5"

Target Market(s)

Gourmet stores, market stall, local tourist market, potential store door sales

Requirements
Must have
• - A design that can be used on various packaging, jars and containers. We are hoping to scale up the production and want something to suit.
• - has to have a wow to stand out on the supermarket shelves
Nice to have
• Things we like:
• Minimalist designs
• Clever designs
• We don't like hand drawn font types
• We are open to the use of a hexagon in the logo, but not must have
Should not have
• Things we do not like:
• Too many colors

```html
<!DOCTYPE html>
<html lang="en">
<head>
<meta charset="utf-8">
<title>Maple Hollow Honey – Label Options</title>
<link href="https://fonts.googleapis.com/css2?family=Comfortaa:wght@500&family=Teko:wght@400&family=Roboto:wght@400&family=Cinzel:wght@500&display=swap" rel="stylesheet">
<style>
  :root {
    --bg: #f2f2ef;
    --gold: #f4ad1a;
    --orange: #ef8a12;
    --rust: #e0561b;
    --ink: #1d1d1d;
    --white-label: #ffffff;
    --cream-label: #efe8d5;
    --black-label: #0f0f0f;
    --silver: #c4c4c4;
  }
  * { margin: 0; padding: 0; box-sizing: border-box; }
  html, body { width: 1200px; height: 912px; overflow: hidden; background: var(--bg); }
  .canvas { position: relative; width: 1200px; height: 912px; }

  .brand-seal {
    position: absolute; left: 520px; top: 24px; width: 160px; height: 160px;
    border: 3px solid var(--gold); border-radius: 50%;
    display: flex; align-items: center; justify-content: center; text-align: center;
  }
  .brand-name {
    font-family: "Comfortaa", sans-serif; font-weight: 500; color: var(--orange);
    font-size: 22px; line-height: 1.05;
  }

  .label { position: absolute; top: 360px; width: 216px; height: 432px; }
  .label svg.shape { position: absolute; inset: 0; }
  .label .content { position: absolute; inset: 0; text-align: center; }

  .label .seal {
    position: absolute; left: 50px; top: 48px; width: 116px; height: 116px;
    border: 2px solid var(--gold); border-radius: 50%;
    display: flex; align-items: center; justify-content: center;
  }
  .label .seal .brand-name { font-size: 16px; }

  .headline {
    position: absolute; left: 0; right: 0; top: 186px;
    font-family: "Teko", sans-serif; font-weight: 400; font-size: 46px; line-height: 0.86;
    letter-spacing: 1px;
  }
  .headline .pure { display: block; color: var(--ink); }
  .headline .raw { display: block; color: var(--orange); }

  .divider { position: absolute; left: 34px; right: 34px; top: 282px; height: 1px; background: var(--orange); }
  .divider::after {
    content: ""; position: absolute; left: 50%; top: -3px; width: 7px; height: 7px;
    margin-left: -3.5px; transform: rotate(45deg); border: 1px solid var(--orange); background: inherit;
  }

  .net-wt {
    position: absolute; left: 0; right: 0; top: 298px;
    font-family: "Teko", sans-serif; font-size: 11px; letter-spacing: 0.5px; color: var(--ink);
  }
  .address {
    position: absolute; left: 0; right: 0; top: 314px;
    font-family: "Cinzel", serif; font-weight: 500; font-size: 10px; letter-spacing: 0.4px; color: var(--rust);
  }
  .quality-badge {
    position: absolute; left: 44px; top: 340px; width: 28px; height: 28px; border-radius: 50%;
    background: var(--ink); border: 2px solid var(--gold);
  }

  .label--black .headline .pure,
  .label--black .net-wt { color: var(--silver); }
  .label--black .quality-badge { background: #2a2a2a; }

  .caption {
    position: absolute; top: 854px; width: 200px; text-align: center;
    font-family: "Roboto", sans-serif; font-size: 22px; color: var(--ink);
  }
</style>
</head>
<body>
<main class="canvas">

  <div class="brand-seal">
    <span class="brand-name">maple hollow<br>honey</span>
  </div>

  <!-- Option 1: white -->
  <section class="label label--white" style="left:130px">
    <svg class="shape" width="216" height="432" viewBox="0 0 216 432">
      <ellipse cx="108" cy="216" rx="107" ry="215" fill="var(--gold)"/>
      <ellipse cx="108" cy="216" rx="99" ry="207" fill="var(--white-label)"/>
      <ellipse cx="108" cy="216" rx="94" ry="202" fill="none" stroke="var(--gold)" stroke-width="1"/>
    </svg>
    <div class="content">
      <div class="seal"><span class="brand-name">maple hollow<br>honey</span></div>
      <h2 class="headline"><span class="pure">100% PURE</span><span class="raw">RAW HONEY</span></h2>
      <div class="divider" style="background:var(--orange)"></div>
      <p class="net-wt">NET WT: 16 OZ (454 G)</p>
      <p class="address">CEDAR RIDGE, MN 56410</p>
      <div class="quality-badge"></div>
    </div>
  </section>

  <!-- Option 2: cream -->
  <section class="label label--cream" style="left:500px">
    <svg class="shape" width="216" height="432" viewBox="0 0 216 432">
      <ellipse cx="108" cy="216" rx="107" ry="215" fill="var(--gold)"/>
      <ellipse cx="108" cy="216" rx="99" ry="207" fill="var(--cream-label)"/>
      <ellipse cx="108" cy="216" rx="94" ry="202" fill="none" stroke="var(--gold)" stroke-width="1"/>
    </svg>
    <div class="content">
      <div class="seal"><span class="brand-name">maple hollow<br>honey</span></div>
      <h2 class="headline"><span class="pure">100% PURE</span><span class="raw">RAW HONEY</span></h2>
      <div class="divider"></div>
      <p class="net-wt">NET WT: 16 OZ (454 G)</p>
      <p class="address">CEDAR RIDGE, MN 56410</p>
      <div class="quality-badge"></div>
    </div>
  </section>

  <!-- Option 3: black -->
  <section class="label label--black" style="left:872px">
    <svg class="shape" width="216" height="432" viewBox="0 0 216 432">
      <ellipse cx="108" cy="216" rx="107" ry="215" fill="var(--gold)"/>
      <ellipse cx="108" cy="216" rx="99" ry="207" fill="var(--black-label)"/>
      <ellipse cx="108" cy="216" rx="94" ry="202" fill="none" stroke="var(--gold)" stroke-width="1"/>
    </svg>
    <div class="content">
      <div class="seal"><span class="brand-name">maple hollow<br>honey</span></div>
      <h2 class="headline"><span class="pure">100% PURE</span><span class="raw">RAW HONEY</span></h2>
      <div class="divider"></div>
      <p class="net-wt">NET WT: 16 OZ (454 G)</p>
      <p class="address">CEDAR RIDGE, MN 56410</p>
      <div class="quality-badge"></div>
    </div>
  </section>

  <p class="caption" style="left:138px">Option 1</p>
  <p class="caption" style="left:508px">Option 2</p>
  <p class="caption" style="left:880px">Option 3</p>

</main>
</body>
</html>
```